I need a website built for my organization.
We are the world's largest network of music producers.
The website should be professional, sharp, and high quality., We need a website built for The Harbor Sound Guild. We are one of the World's largest association of music producers.
The site must be professional, sharp, and high quality., I need a website built for my organization.
The site must be professional, sharp, and high quality.
Somewhere in the top half of the site there should be a form for the user to fill out. The details of the form are as follows:
Title (large and bold): Contact Us or Submit Your Music
Fields to include (* = required): First Name*, Last Name*, Age, Zip Code, Email Address*, Daytime Phone, Evening Phone, Comments
Then, there will be a "submit" button to proceed to next step of form. Just below the "submit" button, should be the following verbiage: "After submitting, you will have the opportunity to upload demos of your music (optional) and provide other pertinent information about yourself, band, or group."
Target Market(s)
Music producers and aspiring musicians
Industry/Entity Type
Group
Colors
Designer to choose colors to be used in the design.
Look and feel
Each slider illustrates characteristics of the customer's brand and the style your logo design should communicate.

```html
<!DOCTYPE html>
<html lang="en">
<head>
<meta charset="utf-8">
<title>The Harbor Sound Guild</title>
<link href="https://fonts.googleapis.com/css2?family=Ubuntu:ital,wght@0,300;0,400;0,500;0,700;1,300;1,400&family=Marcellus&display=swap" rel="stylesheet">
<style>
:root{
  --bg:#000;
  --gold:#b3a57f;
  --gold-dark:#7b7054;
  --gold-text:#a99b73;
  --ink:#fff;
  --muted:#cfcfcf;
  --red:#c8391f;
  --field:#fff;
  --field-text:#9a9a9a;
  --footer-ink:#2b2418;
}
*{box-sizing:border-box;margin:0;padding:0}
html,body{width:813px;height:1200px;overflow:hidden;background:var(--bg)}
body{position:relative;font-family:'Ubuntu',sans-serif;color:var(--ink)}
.abs{position:absolute}

/* hero */
.hero-photo{left:0;top:0;width:813px;height:400px;
  background:radial-gradient(ellipse at 78% 45%,#3d4a44 0%,#1c2220 35%,#0a0a0a 70%),#000}
.hero-fade{left:0;top:300px;width:813px;height:140px;background:linear-gradient(transparent,#000)}
.nav{left:106px;top:0;display:flex;gap:0}
.nav a{display:block;color:var(--ink);text-decoration:none;font-size:13px;line-height:16px;padding-top:18px;margin-right:0}
.nav a b{display:block;color:var(--gold);font-size:16px;font-weight:700}
.nav .active{border-top:3px solid var(--gold);padding-top:15px}
.nav-who{width:85px}.nav-what{width:78px}.nav-event{width:84px}.nav-how{width:69px}
.topbar{left:541px;top:0;width:184px;height:20px;background:var(--gold);border-radius:0 0 14px 14px;font-size:10px;color:#fff}
.topbar .login{left:22px;top:4px}
.topbar .search{left:54px;top:0;width:110px;height:20px;background:#8a7f60;border-radius:0 0 12px 12px;padding:4px 0 0 21px}
.dots{display:flex;gap:5px}
.dots i{width:7px;height:7px;border-radius:50%;background:#ddd;display:block}
.dots i.on{background:var(--red)}
.brand-mark{left:84px;top:82px;width:88px;height:88px;border-radius:50%;background:var(--gold)}
.brand-name{left:190px;top:92px;font-family:'Marcellus',serif}
.brand-name .l1{font-size:40px;line-height:44px;color:#fff}
.brand-name .l2{font-size:19px;color:var(--gold)}
.arrow{top:188px}

/* events */
.events-tab{left:81px;top:302px;width:97px;height:24px;background:#fff;color:#000;font-weight:700;font-size:15px;text-align:center;line-height:24px}
.events-strip{left:81px;top:326px;width:650px;height:75px;background:rgba(0,0,0,.55)}
.event{top:346px;width:180px;height:40px}
.event .date{left:0;top:0;width:40px;height:40px;background:var(--gold);color:#222;text-align:center;font-size:14px;line-height:17px;padding-top:3px}
.event .title{left:55px;top:-2px;color:var(--gold);font-size:13px}
.event .desc{left:55px;top:17px;font-size:8px;line-height:10px;color:#fff;width:95px}

/* form */
.form-title{left:83px;top:430px;font-size:26px;font-weight:500}
.form-title span,.accent{color:var(--gold-text)}
.field{height:20px;background:var(--field);color:var(--field-text);font-size:11px;padding:4px 8px;font-weight:300}
.req{color:#fff;font-size:10px}
.crowd{left:515px;top:445px;width:266px;height:138px;background:radial-gradient(ellipse at 55% 30%,#8d8d8d 0%,#3a3a3a 40%,#000 80%)}
.submit{left:523px;top:583px;width:207px;height:29px;background:var(--gold);font-weight:700;font-size:20px;text-align:center;line-height:30px;letter-spacing:.5px}
.note{left:87px;top:623px;font-size:8.5px;color:var(--gold-text)}

/* welcome */
.portrait{left:85px;top:668px;width:260px;height:238px;background:radial-gradient(ellipse at 50% 40%,#4a4a4a 0%,#1d1d1d 50%,#000 85%)}
.welcome-title{left:358px;top:680px;font-size:31px;font-weight:500}
.welcome-body{left:358px;top:732px;width:373px;font-size:9.3px;line-height:11.8px;color:#fff}
.welcome-body p+p{margin-top:12px}

/* columns */
.col{top:933px;width:205px;border-top:1px solid #555}
.col h3{font-size:18px;font-weight:700;margin-top:14px}
.col .dots{position:absolute;right:2px;top:21px}
.news-item{display:flex;align-items:flex-start;margin-top:9px;font-size:12px}
.news-item .d{background:var(--gold-dark);width:74px;height:18px;font-size:12px;text-align:center;line-height:18px;margin-right:7px;flex:none}
.news-item .t{line-height:14px;padding-top:2px}
.feed p{font-style:italic;font-weight:300;font-size:11px;line-height:14px;margin-top:10px}
.feed .ago{color:var(--red);margin-top:3px}
.avatar{left:524px;top:985px;width:76px;height:76px;border-radius:50%;background:radial-gradient(circle at 50% 45%,#777 0%,#3b3b3b 55%,#1a1a1a 100%);border:2px solid #555}
.quote{left:609px;top:981px;width:120px;font-style:italic;font-weight:300;font-size:11px;line-height:14px}
.who-name{left:609px;top:1081px;color:var(--red);font-size:10px;font-weight:700}
.who-role{left:609px;top:1093px;color:var(--red);font-size:9px;font-style:italic}

/* footer */
.footer{left:0;top:1122px;width:813px;height:78px;background:var(--gold)}
.footer-mark{left:82px;top:12px;width:54px;height:54px;border-radius:50%;background:#fff}
.footer-name{left:144px;top:16px;font-family:'Marcellus',serif;color:#fff}
.footer-name .l1{font-size:24px;line-height:26px}
.footer-name .l2{font-size:12px}
.social{top:11px;width:27px;height:27px}
.copy{right:84px;top:44px;font-size:8.5px;color:var(--footer-ink)}
.links{right:84px;top:60px;font-size:8.5px;color:var(--footer-ink)}
</style>
</head>
<body>

<div class="abs hero-photo" role="img" aria-label="Concert photo of a DJ in headphones above a stage crowd"></div>
<div class="abs hero-fade"></div>

<nav class="abs nav">
  <a class="nav-who active" href="#"><b>Who</b>we are</a>
  <a class="nav-what" href="#"><b>What</b>we do</a>
  <a class="nav-event" href="#"><b>Event</b>&amp; news</a>
  <a class="nav-how" href="#"><b>How</b>to join</a>
  <a href="#"><b>Contact</b>us</a>
</nav>

<div class="abs topbar">
  <span class="abs login">login</span>
  <div class="abs search">Search here
    <svg class="abs" style="left:95px;top:3px" width="13" height="13" viewBox="0 0 13 13"><circle cx="7.5" cy="5.5" r="4.2" fill="none" stroke="#fff" stroke-width="1.4"/><line x1="4.5" y1="8.5" x2="1" y2="12" stroke="#fff" stroke-width="1.6"/></svg>
  </div>
</div>

<div class="abs dots" style="left:666px;top:54px"><i class="on"></i><i></i><i></i><i></i><i></i></div>

<div class="abs brand-mark"></div>
<div class="abs brand-name"><div class="l1">The Harbor</div><div class="l2">Sound Guild</div></div>

<svg class="abs arrow" style="left:25px" width="14" height="20" viewBox="0 0 14 20"><polyline points="11,2 3,10 11,18" fill="none" stroke="#fff" stroke-width="3"/></svg>
<svg class="abs arrow" style="left:772px" width="14" height="20" viewBox="0 0 14 20"><polyline points="3,2 11,10 3,18" fill="none" stroke="#fff" stroke-width="3"/></svg>

<div class="abs events-strip"></div>
<div class="abs events-tab">Events</div>
<svg class="abs" style="left:94px;top:343px" width="16" height="48" viewBox="0 0 16 48"><polyline points="15,1 2,24 15,47" fill="none" stroke="#888" stroke-width="1"/></svg>
<svg class="abs" style="left:703px;top:343px" width="16" height="48" viewBox="0 0 16 48"><polyline points="1,1 14,24 1,47" fill="none" stroke="#888" stroke-width="1"/></svg>

<div class="abs event" style="left:137px"><div class="abs date">4<br>Nov</div><div class="abs title">Power Festival</div><div class="abs desc">Nulla non diam a metus viverra volutpat ac nec lacus. Integer ut lectus</div></div>
<div class="abs event" style="left:332px"><div class="abs date">4<br>Nov</div><div class="abs title">Power Festival</div><div class="abs desc">Nulla non diam a metus viverra volutpat ac nec lacus. Integer ut lectus</div></div>
<div class="abs event" style="left:524px"><div class="abs date">4<br>Nov</div><div class="abs title">Power Festival</div><div class="abs desc">Nulla non diam a metus viverra volutpat ac nec lacus. Integer ut lectus</div></div>

<div class="abs crowd" role="img" aria-label="Photo of a fan raising both arms before stage lights"></div>
<h2 class="abs form-title">Submit <span>Music Demo</span></h2>

<div class="abs field" style="left:81px;top:473px;width:208px">First name</div>
<span class="abs req" style="left:291px;top:463px">*</span>
<div class="abs field" style="left:303px;top:473px;width:206px">Last name</div>
<span class="abs req" style="left:510px;top:463px">*</span>
<div class="abs field" style="left:81px;top:504px;width:96px">Age</div>
<div class="abs field" style="left:192px;top:504px;width:97px">Zip Code</div>
<div class="abs field" style="left:303px;top:504px;width:206px">Email Address</div>
<span class="abs req" style="left:510px;top:500px">*</span>
<div class="abs field" style="left:81px;top:533px;width:208px">Daytime Phone</div>
<div class="abs field" style="left:303px;top:533px;width:206px">Evening Phone</div>
<div class="abs field" style="left:81px;top:562px;width:428px;height:50px">Comments</div>

<div class="abs submit">SUBMIT</div>
<p class="abs note">After submitting, you will have the opportunity to upload demos of your music (optional) and provide other pertinent information about yourself, band, or group.</p>

<div class="abs portrait" role="img" aria-label="Photo of a producer wearing a beanie, sunglasses and headphones"></div>
<h2 class="abs welcome-title">Welcome <span class="accent">Marlowe</span></h2>
<div class="abs welcome-body">
  <p>Lorem ipsum dolor sit amet, consectetur adipiscing elit. Sed adipiscing sit amet sem sit amet viverra. Cras porta justo risus, quis sodales diam placerat vitae. Quisque eget dui orci. Cras aliquet, odio quis gravida fermentum, nibh lorem vulputate nunc, ut condi-mentum mauris ipsum non ipsum. Duis eleifend mauris nibh, ac hendrerit nisi bibendum dignissim. Nullam blandit urna vulputate nisl dignissim, vel tempus ante porttitor. Sed sed mi ac eros viverra rhoncus. Sed tempor sodales libero sit amet con-vallis.</p>
  <p>Morbi ac lectus lectus. Proin vitae facilisis enim. Suspendisse a fermentum magna. Curabitur accumsan ac magna ac vehicula. Sed sollicitudin, magna sed commodo pretium, arcu nunc tincidunt sem, quis laoreet felis eros et arcu. Maecenas porta tempus vulputate. Sed iaculis orci adipiscing lectus molestie dignissim. In vehicula, libero sit amet dapibus luctus, felis massa tincidunt eros, sodales fringilla lorem sem nec diam.</p>
</div>

<section class="abs col" style="left:84px">
  <h3>Latest <span class="accent">News</span></h3>
  <div class="dots"><i class="on"></i><i></i><i></i></div>
  <div class="news-item" style="margin-top:12px"><span class="d">03/08/2014</span><span class="t">Quisque nisl metus,</span></div>
  <div class="news-item"><span class="d">03/08/2014</span><span class="t">Rhoncus facilisis</span></div>
  <div class="news-item"><span class="d">03/08/2014</span><span class="t">Porta condimentum</span></div>
  <div class="news-item"><span class="d">03/08/2014</span><span class="t">Quisque pharetra sodales dapibus.</span></div>
</section>

<section class="abs col feed" style="left:304px">
  <h3 style="margin-left:6px">Chirp <span class="accent">Feed</span></h3>
  <div class="dots"><i class="on"></i><i></i><i></i></div>
  <p style="margin-left:4px">Quisque nisl metus, rhoncus facilisis metus a, porta condimentum orci. Sed sit amet interdum lectus. Quisque dignissim massa</p>
  <p class="ago" style="margin-left:4px">2 days ago</p>
  <p style="margin-left:4px;margin-top:12px">Curabitur a lorem luctus, faucibus dui ac, consectetur turpis. Aenean cursus velit ac</p>
  <p class="ago" style="margin-left:4px;margin-top:8px">2 days ago</p>
</section>

<section class="abs col" style="left:524px">
  <h3 style="margin-left:2px"><span class="accent">Testimonial</span></h3>
  <div class="dots"><i class="on"></i><i></i><i></i></div>
</section>
<div class="abs avatar" role="img" aria-label="Portrait photo of the quoted music producer"></div>
<p class="abs quote">“ Quisque nisl metus, rhoncus facilisis metus a, porta condimentum orci. Sed sit amet interdum lectus. Quisque dignissim massa et sollicitudin</p>
<span class="abs who-name">Elias</span>
<span class="abs who-role">Music Producer</span>

<footer class="abs footer">
  <div class="abs footer-mark"></div>
  <div class="abs footer-name"><div class="l1">The Harbor</div><div class="l2">Sound Guild</div></div>
  <div class="abs social" style="left:635px;background:#3b5b9a" role="img" aria-label="Social link one"></div>
  <div class="abs social" style="left:668px;background:#2ba1d6" role="img" aria-label="Social link two"></div>
  <div class="abs social" style="left:701px;background:#d3362b" role="img" aria-label="Social link three"></div>
  <p class="abs copy">Copyright 2013 © Harbor Associates. Power by Northlight Studio</p>
  <p class="abs links">Privacy Policy | &nbsp;Terms and Conditions | &nbsp;Site Map | &nbsp;Feedback | &nbsp;Report Bug | &nbsp;Contact Us</p>
</footer>

</body>
</html>
```